New Zealand Luggage Importer Needs Business Cards

We need professional, creative and fashionable business cards created.
We are based in New Zealand and import and distribute high-end, quality, fashionable and durable luggage.
We pride ourselves on selling the very best quality luggage, second only to 1 brand (which we won't mention here)...we use the same manufacturer. However, our prices are much more reasonable.
Industry/Entity Type
Business
Contact Information for Business Card
Mark Dunsley
027 512 4068
3/17 Harlow Street, Pinecrest Flats, Auckland, 0614
PO Box 204377, Fernside, Auckland 0731
09-528-3916
sales@brivancases.co.nz / www.brivancases.co.nz

```html
<!DOCTYPE html>
<html lang="en">
<head>
<meta charset="utf-8">
<title>Brivan Cases — Business Cards</title>
<link rel="stylesheet" href="https://fonts.googleapis.com/css2?family=Arimo:wght@400;700&display=swap">
<style>
  :root {
    --stage: #2b2b2b;
    --card-black: #050505;
    --card-white: #f1f0ee;
    --ink: #111111;
    --gold: #c9a84f;
    --gold-light: #e2c877;
    --band: #7b6f52;
    --white: #ffffff;
  }
  * { box-sizing: border-box; margin: 0; padding: 0; }
  html, body { width: 1200px; height: 900px; overflow: hidden; }
  body {
    background: var(--stage);
    font-family: "Arimo", Arial, sans-serif;
    position: relative;
  }
  .card {
    position: absolute;
    width: 520px;
    height: 300px;
    border-radius: 3px;
    box-shadow: 0 10px 24px rgba(0,0,0,0.45);
    overflow: hidden;
  }
  .card--front { left: 70px; top: 90px; background: var(--card-black); }
  .card--back { left: 610px; top: 360px; background: var(--card-white); }

  .wordmark {
    font-weight: 700;
    letter-spacing: 0.04em;
    white-space: nowrap;
    position: absolute;
  }
  .card--front .wordmark { color: var(--white); font-size: 42px; left: 70px; top: 118px; }
  .card--back .wordmark { color: var(--ink); font-size: 26px; left: 40px; top: 38px; }

  .gold-rule {
    position: absolute;
    left: 0;
    right: 0;
    height: 4px;
    background: linear-gradient(90deg, var(--gold), var(--gold-light), var(--gold));
  }
  .gold-rule::before,
  .gold-rule::after {
    content: "";
    position: absolute;
    width: 4px;
    height: 14px;
    background: var(--gold);
  }
  .gold-rule::before { left: 0; top: 0; }
  .gold-rule::after { right: 0; bottom: 0; }
  .card--front .gold-rule { bottom: 34px; }
  .card--back .gold-rule { bottom: 26px; }

  .contact { position: absolute; left: 40px; top: 92px; }
  .contact__name {
    color: var(--gold);
    font-weight: 700;
    font-size: 20px;
    margin-bottom: 12px;
  }
  .contact__lines {
    list-style: none;
    color: var(--ink);
    font-size: 12.5px;
    line-height: 1.45;
  }
  .contact__web {
    list-style: none;
    margin-top: 18px;
    color: var(--gold);
    font-weight: 700;
    font-size: 12.5px;
    line-height: 1.45;
  }

  .brand-lockup {
    position: absolute;
    left: 56px;
    top: 748px;
    color: var(--white);
    font-size: 40px;
  }
  .floor-band {
    position: absolute;
    left: 0;
    right: 0;
    top: 828px;
    height: 22px;
    background: var(--band);
  }
</style>
</head>
<body>
  <section class="card card--front" aria-label="Card front">
    <div class="wordmark">BRIVAN CASES</div>
    <div class="gold-rule"></div>
  </section>

  <section class="card card--back" aria-label="Card back">
    <div class="wordmark">BRIVAN CASES</div>
    <div class="contact">
      <p class="contact__name">Mark Dunsley</p>
      <ul class="contact__lines">
        <li>027 512 4068</li>
        <li>3/17 Harlow Street, Pinecrest Flats, Auckland, 0614</li>
        <li>PO Box 204377, Fernside, Auckland 0731</li>
        <li>09-528-3916</li>
      </ul>
      <ul class="contact__web">
        <li>sales@brivancases.co.nz</li>
        <li>www.brivancases.co.nz</li>
      </ul>
    </div>
    <div class="gold-rule"></div>
  </section>

  <div class="wordmark brand-lockup">BRIVAN CASES</div>
  <div class="floor-band"></div>
</body>
</html>
```